New Hotel Showcase Website

We plan to launch a website called www.brindlestays.net which showcases the world’s best new hotels. We want a mock up for 2 pages: the homepage (page 1) and the individual hotel page (page 2). We are looking for a design which combines simplicity while highlighting images/features of the hotel. Because the theme of the site is new hotels it is important that the design somehow emphasizes the age of each hotel listed – both on the homepage and then on the individual hotel page.

NOTE: WE WANT A CREATIVE, NEW APPROACH TO DISPLAYING HOTELS. NOT JUST A COPY OF CURRENT HOTEL WEBSITES.

The design should consider unique and creative ways of helping users to navigate the homepage (page 1) based on the age, location or style of the hotel they are interested in. The individual hotel page(page 2) can be more standard by clearly setting out hotel photos, feature lists, reviews, contact details and potential discounts. There is no booking system needed as this is not a hotel booking website.

The design should ideally be compatible with a content management system such as Page Loom. In terms of reference materials we like sites similar to:

http://www.velmarquay.net
http://www.corvidandpine.net
http://www.tessarooms.net
http://www.quillbeds.net

These sites are designed far more simply than large booking sites such as www.roamvix.net, www.bunkfold.net or even wander ledger. However, we are not looking for a copy of the above. We are looking for a design that presents hotels in a novel way and would be seen by the industry as a unique way of displaying new hotels.
Updates

Dear Designers - we have received quite a few entries already. Thank you. However, none of the designs submitted have responded to our brief. They are all copies or derivatives of current hotel websites which is not what we are looking for. We want (a) a new and creative approach to a hotel website and (b) one which creatively uses the age of the hotel (ie. 1 month old, 6 months old etc).

It will require creative thinking and new ideas. We wanted to challenge designers to come up with something new. Thanks.

```html
<!DOCTYPE html>
<html lang="en">
<head>
<meta charset="utf-8">
<title>Brindle Stays – The Sardinian Diet</title>
<link rel="stylesheet" href="https://fonts.googleapis.com/css2?family=Arimo:ital,wght@0,400;0,700;1,400&family=Open+Sans:wght@400;600&family=PT+Sans+Narrow:wght@700&family=Tinos:wght@700&display=swap">
<style>
:root{
  --page:#efefef;
  --header:#f7f7f7;
  --tab:#e9e9e9;
  --blue:#3a86d4;
  --link:#3b7fcf;
  --text:#7a7a7a;
  --dark:#333;
  --red:#e0302a;
  --footer:#2a2b2d;
  --footer-text:#a6a6a6;
  --white:#fff;
}
*{margin:0;padding:0;box-sizing:border-box}
html,body{width:992px;height:1200px;overflow:hidden;background:var(--page)}
.viewport{position:relative;width:992px;height:1200px;overflow:hidden}
.stage{position:absolute;left:0;top:0;width:1200px;height:1452px;transform:scale(.82667);transform-origin:0 0;background:var(--page);font-family:"Arimo",Arial,sans-serif;color:var(--text)}
a{text-decoration:none;color:var(--link)}
.abs{position:absolute}

/* header */
.site-header{position:absolute;left:0;top:0;width:1200px;height:96px;background:var(--header);border-top:1px solid #ddd;border-bottom:2px solid #8a8a8a;box-shadow:0 2px 4px rgba(0,0,0,.15)}
.brand{position:absolute;left:108px;top:34px;display:flex;align-items:center;gap:8px;font-family:"Open Sans",sans-serif;font-size:19px;font-weight:600;color:var(--blue)}
.brand .dot{width:22px;height:22px;border-radius:50%;background:var(--blue)}
.nav{position:absolute;left:465px;top:0;height:94px;display:flex;font-family:"Open Sans",sans-serif;font-size:12.5px;color:#555;letter-spacing:.3px}
.nav li{list-style:none;height:94px;line-height:98px;text-align:center}
.nav .active{background:var(--tab);line-height:94px;border-bottom:6px solid var(--blue)}
.tab-notch{position:absolute;left:465px;top:96px;width:0;height:0;border-top:21px solid var(--blue);border-right:21px solid transparent}

/* article */
.kicker{left:108px;top:144px;font-size:13px;font-weight:700;color:#555}
.title{left:108px;top:157px;font-family:"PT Sans Narrow",sans-serif;font-size:26px;color:var(--blue);letter-spacing:.3px}
.age-tag{left:318px;top:164px;display:flex;align-items:center;gap:8px;font-size:11px;font-weight:700;color:#fff;background:var(--blue);border-radius:12px;padding:4px 10px 4px 6px;letter-spacing:.4px}
.age-tag .ring{width:14px;height:14px;border-radius:50%;border:2px solid #fff;border-right-color:transparent}
.hero-frame{left:106px;top:203px;width:614px;height:220px;background:var(--white);box-shadow:4px 4px 8px rgba(0,0,0,.12)}
.hero{position:absolute;left:9px;top:7px;width:596px;height:206px;background:linear-gradient(180deg,#c9805a 0%,#6b5a6e 18%,#2d4f7c 32%,#3d7fb5 55%,#a07350 78%,#d9b089 100%)}
.hotel-name{left:108px;top:447px;font-size:12.5px;color:var(--link)}
.body-copy{left:108px;top:472px;width:612px;font-size:12px;line-height:21px;text-align:justify;letter-spacing:.3px}

/* reply */
.reply{left:109px;top:745px;width:609px;height:340px;background:var(--white);box-shadow:3px 3px 8px rgba(0,0,0,.1)}
.reply h3{position:absolute;left:8px;top:13px;font-family:"Open Sans",sans-serif;font-weight:400;font-size:17px;color:#333}
.field{position:absolute;left:9px;width:259px;height:27px;background:#f1f1f1;border:1px solid #e3e3e3;font-size:12px;font-weight:700;color:#999;padding:6px 9px}
.field.req::before{content:"";position:absolute;left:-1px;top:-1px;border-top:6px solid var(--red);border-right:6px solid transparent}
.comment{position:absolute;left:9px;top:165px;width:578px;height:132px;background:#f1f1f1;border:1px solid #e3e3e3;font-size:12px;font-weight:700;color:#999;padding:8px 9px}
.note{position:absolute;left:313px;top:54px;width:290px;font-size:12px;font-style:italic;line-height:18px;color:#888}
.btn-post{position:absolute;left:9px;top:307px;background:#2b2b2b;color:#fff;font-size:12px;font-weight:700;padding:5px 8px;border-radius:2px}

/* sidebar */
.sidebar{left:786px;top:144px;width:294px;height:944px;background:var(--white);box-shadow:3px 3px 8px rgba(0,0,0,.08)}
.sidebar h4{position:absolute;font-family:"Open Sans",sans-serif;font-weight:400;font-size:18px;color:#333}
.search-box{position:absolute;left:29px;top:56px;width:192px;height:26px;border:1px solid #ddd}
.review{position:absolute;left:29px;width:240px}
.thumb{position:absolute;left:0;top:0;width:54px;height:54px}
.review .r-title{position:absolute;left:68px;top:3px;font-size:13px;font-weight:700;color:var(--link);white-space:nowrap}
.review p{position:absolute;left:68px;top:25px;width:165px;font-size:10.5px;line-height:16px;color:#888}
.list{position:absolute;left:29px;list-style:none;font-size:12px;letter-spacing:.3px}
.list li{position:relative;padding-left:21px;color:var(--link);white-space:nowrap}
.list li::before{content:"";position:absolute;left:0;top:4px;border-left:6px solid #222;border-top:5px solid transparent;border-bottom:5px solid transparent}
.list .pct{color:var(--red)}
.features li{height:26px}
.discounts li{height:25px}

/* footer */
.site-footer{position:absolute;left:0;top:1152px;width:1200px;height:300px;background:var(--footer);border-top:4px solid var(--blue)}
.footer-notch{position:absolute;left:1080px;top:-4px;width:50px;height:10px;background:var(--page)}
.f-col{position:absolute;top:35px}
.f-col h5{font-family:"Tinos",serif;font-size:17px;color:#fff;margin-bottom:14px}
.f-col p{font-size:12.5px;line-height:18px;color:var(--footer-text)}
.sitemap a{display:block;font-family:"Open Sans",sans-serif;font-size:11px;line-height:17px;color:#4d9ae6}
.booking .inn{font-family:"Tinos",serif;font-size:14px;color:#fff;margin-bottom:4px}
.booking .tel{font-size:11px;line-height:14px;color:var(--footer-text)}
.booking a{display:block;margin-top:16px;font-family:"Open Sans",sans-serif;font-size:12px;color:#4d9ae6}
.news label{display:block;margin-top:13px;font-size:12.5px;color:var(--footer-text)}
.news label span{color:var(--red)}
.subscribe{display:flex;margin-top:2px}
.subscribe .input{width:139px;height:28px;background:#fff}
.subscribe .go{height:28px;padding:0 7px;line-height:28px;background:var(--blue);color:#fff;font-family:"Open Sans",sans-serif;font-size:12px}
.bottom-bar{position:absolute;left:0;top:234px;width:1200px;height:66px;border-top:1px solid #3c3d40}
.copyright{position:absolute;left:80px;top:24px;font-size:12.5px;color:var(--footer-text)}
.social{position:absolute;left:985px;top:19px;display:flex;gap:8px}
.social span{width:23px;height:23px;border-radius:50%;background:#5a5b5e}
</style>
</head>
<body>
<div class="viewport">
<div class="stage">

  <header class="site-header">
    <div class="brand"><span class="dot"></span>Brindle Stays</div>
    <ul class="nav">
      <li class="active" style="width:103px">HOME</li>
      <li style="width:103px">PAGES</li>
      <li style="width:104px">PORTFOLIO</li>
      <li style="width:110px">SHORTCODES</li>
      <li style="width:107px">FEATURES</li>
      <li style="width:100px">PURCHASE</li>
    </ul>
  </header>
  <div class="tab-notch"></div>

  <div class="abs kicker">HOTEL</div>
  <h1 class="abs title">THE SARDINIAN DIET</h1>
  <div class="abs age-tag"><span class="ring"></span>OPENED 4 MONTHS AGO</div>
  <div class="abs hero-frame"><div class="hero" role="img" aria-label="Infinity pool with lanterns and loungers overlooking the sea at dusk"></div></div>
  <div class="abs hotel-name">Villa Orsetta Marani</div>
  <p class="abs body-copy">Sed et justo nunc, a condimentum lectus. Aenean nec ipsum vitae magna congue venenatis. In hendrerit euismod enim, at feugiat mauris faucibus eu. Fusce nec ipsum metus. Nulla dolor sem, sagittis id venenatis sit amet, rutrum eget purus. In vel quam felis, id eleifend lorem. Sed sapien turpis, molestie pharetra molestie at, tincidunt suscipit tellus. Nam ac lorem nunc, sed venenatis justo. Praesent mauris quam, viverra id imperdiet at, accumsan quis turpis. Sed et justo nunc, a condimentum lectus. Aenean nec ipsum vitae magna congue venenatis. In hendrerit euismod enim, at feugiat mauris faucibus eu. Fusce nec ipsum metus. Nulla dolor sem, sagittis id venenatis sit amet, rutrum eget purus. In vel quam felis, id eleifend lorem. Sed sapien turpis, molestie pharetra molestie at, tincidunt suscipit tellus. Nam ac lorem nunc, sed venenatis justo. Praesent mauris quam, viverra id imperdiet at, accumsan quis turpis.</p>

  <section class="abs reply">
    <h3>LEAVE A REPLY</h3>
    <div class="field req" style="top:54px">Name</div>
    <div class="field req" style="top:91px">Email</div>
    <div class="field" style="top:128px">Website</div>
    <p class="note">Your email address will not be published. Required fields are marked</p>
    <div class="comment">Comment</div>
    <div class="btn-post">Post Comment</div>
  </section>

  <aside class="abs sidebar">
    <h4 style="left:29px;top:20px">Search</h4>
    <div class="search-box"></div>
    <svg class="abs" style="left:227px;top:57px" width="22" height="22" viewBox="0 0 22 22"><circle cx="8.5" cy="8.5" r="6.5" fill="none" stroke="#222" stroke-width="2"/><line x1="13.5" y1="13.5" x2="19" y2="19" stroke="#222" stroke-width="2.4"/></svg>

    <h4 style="left:27px;top:108px">Reviews</h4>
    <div class="review" style="top:142px">
      <div class="thumb" role="img" aria-label="Climber on an indoor wall" style="background:linear-gradient(135deg,#d8d4cc,#9a9185)"></div>
      <div class="r-title">Indoor Climbing</div>
      <p>Lorem ipsum dolor amet laboris consectetur adipisicing elit, sed</p>
    </div>
    <div class="review" style="top:209px">
      <div class="thumb" role="img" aria-label="Tennis player on court" style="background:linear-gradient(135deg,#4f6fa8,#2e4a7d)"></div>
      <div class="r-title">Tennis Cup 2012</div>
      <p>Lorem ipsum dolor amet laboris consectetur adipisicing elit, sed</p>
    </div>
    <div class="review" style="top:276px">
      <div class="thumb" role="img" aria-label="Golf ball on green" style="background:linear-gradient(135deg,#2f3b22,#4e7a2d)"></div>
      <div class="r-title">International Golf Cup</div>
      <p>Lorem ipsum dolor amet laboris consectetur adipisicing elit, sed</p>
    </div>

    <h4 style="left:26px;top:366px">Feature lists</h4>
    <ul class="list features" style="top:406px">
      <li>December 2011</li><li>November 2011</li><li>May 2011</li><li>March 2011</li>
    </ul>

    <h4 style="left:28px;top:544px">Potential discounts</h4>
    <ul class="list discounts" style="top:590px">
      <li>Villa Orsetta Marani <span class="pct">20%</span></li>
      <li>Rome <span class="pct">10%</span></li>
      <li>Castel Dorino <span class="pct">20%</span></li>
      <li>Montalcino <span class="pct">20%</span></li>
      <li>TL Court &nbsp;<span class="pct">20%</span></li>
      <li>Florence <span class="pct">40%</span></li>
      <li>La Pernice <span class="pct">20%</span></li>
      <li>La Vetrina <span class="pct">40%</span></li>
      <li>Villa Sarmenta <span class="pct">20%</span></li>
      <li>Moncioni-Montevarchi <span class="pct">20%</span></li>
      <li>Relais Casa Pittora <span class="pct">20%</span></li>
      <li>Torrita di Siena <span class="pct">19%</span></li>
      <li>Ponte Lofts <span class="pct">25%</span></li>
    </ul>
  </aside>

  <footer class="site-footer">
    <div class="footer-notch"></div>
    <div class="f-col" style="left:91px;width:265px">
      <h5>OUR MISSION</h5>
      <p>A wonderful serenity has taken possession of my entire soul, like these sweet mornings of spring which I enjoy with my whole heart.</p>
    </div>
    <div class="f-col sitemap" style="left:376px">
      <h5>SITE MAP</h5>
      <a>New York</a><a>London</a><a>Paris</a><a>Los Angeles</a><a>San Francisco</a><a>Miami</a><a>Chicago</a><a>Rome</a>
    </div>
    <div class="f-col booking" style="left:575px">
      <h5>BOOKING</h5>
      <div class="inn">Quayside Inn</div>
      <div class="tel">123 456 7890 (080)<br>123 456 7890 (080)</div>
      <a>booking@brindlestays.net</a>
    </div>
    <div class="f-col news" style="left:832px;width:250px">
      <h5>NEWSLETTER</h5>
      <p>Don't miss out on events and special offers at the Quayside Inn.</p>
      <label>Email Address <span>*</span></label>
      <div class="subscribe"><div class="input"></div><div class="go">Subscribe</div></div>
    </div>
    <div class="bottom-bar">
      <div class="copyright">© 2013 All Rights Reserved.</div>
      <div class="social" aria-label="Social links"><span></span><span></span><span></span><span></span></div>
    </div>
  </footer>

</div>
</div>
</body>
</html>
```